Stationary for a Manufacturing Company focused on R&D
Twin-Kay please refer to the concluded Logo Project
Stationary for a Manufacturing Company focused on R&D - Manufacturing
Creative Brief
Use same font as used in my logo
Yes please refer to the log - keep the background colors simple
Modern
Vikram Talwarkar
Stationary for a Manufacturing company
Rustomji Parekh Building, 58 Hill Street, Fortm Mumbai 400019 India
vikram@twin-kay.com
www.twin-kay.com
The card must show advancement - something different but easy to duplicate.....
no information on the back - maybe just the logo at the back could be ok

```html
<!DOCTYPE html>
<html lang="en">
<head>
<meta charset="utf-8">
<title>Twin-Kay Business Card</title>
<link rel="stylesheet" href="https://fonts.googleapis.com/css2?family=Michroma&family=Exo+2:wght@400;500&display=swap">
<style>
  :root {
    --page-bg: #e4e6e5;
    --green-dark: #2f5b2a;
    --green-mid: #4f8a45;
    --green-light: #7bb26e;
    --green-pale: #8fb985;
    --ink: #3b3f3d;
    --ink-soft: #6b706d;
    --card-white: #ffffff;
    --arc-grey: #4a4f4c;
    --back-text: #e8efe6;
  }
  * { box-sizing: border-box; margin: 0; padding: 0; }
  html, body { width: 1200px; height: 984px; overflow: hidden; }
  body {
    background: var(--page-bg);
    font-family: "Exo 2", Arial, sans-serif;
    color: var(--ink);
    position: relative;
  }
  .card {
    position: absolute;
    left: 220px;
    width: 760px;
    height: 434px;
    border-radius: 22px;
    overflow: hidden;
  }
  .card-back {
    top: 45px;
    background: radial-gradient(ellipse at 50% 40%, var(--green-light) 0%, var(--green-mid) 45%, var(--green-dark) 100%);
  }
  .card-front {
    top: 509px;
    background: var(--card-white);
  }
  .card-shape { position: absolute; inset: 0; width: 100%; height: 100%; }

  .brand-mark {
    display: inline-flex;
    align-items: center;
    gap: 14px;
    font-family: "Michroma", Arial, sans-serif;
    letter-spacing: 2px;
    white-space: nowrap;
  }
  .brand-dot { width: 30px; height: 30px; border-radius: 50%; flex: none; }

  .back-brand {
    position: absolute;
    top: 160px;
    left: 0; right: 0;
    text-align: center;
  }
  .back-brand .brand-mark { font-size: 34px; color: var(--back-text); }
  .back-brand .brand-dot { background: var(--back-text); width: 40px; height: 40px; }
  .back-web {
    position: absolute;
    top: 262px;
    left: 0; right: 0;
    text-align: center;
    font-family: "Michroma", Arial, sans-serif;
    font-size: 11px;
    letter-spacing: 5px;
    color: var(--back-text);
    text-transform: uppercase;
  }

  .front-brand {
    position: absolute;
    top: 74px;
    left: 40px;
  }
  .front-brand .brand-mark { font-size: 28px; color: var(--ink); }
  .front-brand .brand-dot { background: var(--green-mid); }
  .tagline {
    margin: 6px 0 0 200px;
    font-size: 8px;
    letter-spacing: 1px;
    color: var(--ink-soft);
    text-transform: uppercase;
    white-space: nowrap;
  }
  .contact-list {
    position: absolute;
    top: 160px;
    left: 42px;
    list-style: none;
    font-size: 12px;
    line-height: 19px;
    color: var(--ink);
    white-space: nowrap;
  }
  .contact-list li { display: flex; align-items: center; gap: 9px; }
  .contact-list li.indent { padding-left: 17px; }
  .bullet {
    width: 8px; height: 8px; border-radius: 50%;
    background: var(--green-mid);
    flex: none;
  }
  .person-name {
    position: absolute;
    right: 60px;
    bottom: 46px;
    font-family: "Michroma", Arial, sans-serif;
    font-size: 14px;
    letter-spacing: 4px;
    color: var(--green-mid);
    text-transform: uppercase;
    white-space: nowrap;
  }
</style>
</head>
<body>

  <section class="card card-back" aria-label="Card back">
    <div class="back-brand">
      <span class="brand-mark"><span class="brand-dot"></span>TWIN-KAY</span>
    </div>
    <p class="back-web">www.twin-kay.com</p>
  </section>

  <section class="card card-front" aria-label="Card front">
    <svg class="card-shape" viewBox="0 0 760 434" preserveAspectRatio="none" aria-hidden="true">
      <defs>
        <linearGradient id="swoosh-green" x1="0" y1="0" x2="1" y2="1">
          <stop offset="0" stop-color="#7bb26e"/>
          <stop offset="0.5" stop-color="#4f8a45"/>
          <stop offset="1" stop-color="#2f5b2a"/>
        </linearGradient>
      </defs>
      <path d="M230 0 L760 0 L760 360 C690 240 520 80 230 0 Z" fill="url(#swoosh-green)"/>
      <path d="M0 28 C90 8 170 4 240 6 C180 10 100 22 0 44 Z" fill="var(--arc-grey)"/>
      <path d="M0 50 C110 24 200 18 290 22 C200 26 110 40 0 62 Z" fill="var(--green-pale)" opacity="0.7"/>
    </svg>

    <div class="front-brand">
      <span class="brand-mark"><span class="brand-dot"></span>TWIN-KAY</span>
      <p class="tagline">Engineered by research</p>
    </div>

    <ul class="contact-list">
      <li><span class="bullet"></span>Rustomji Parekh Building,</li>
      <li class="indent">58 Hill Street, Fortm</li>
      <li class="indent">Mumbai 400019 India</li>
      <li><span class="bullet"></span>+91 22 4000 0148</li>
      <li><span class="bullet"></span>+91 98 2000 0371</li>
      <li><span class="bullet"></span>vikram@twin-kay.com</li>
      <li><span class="bullet"></span>www.twin-kay.com</li>
    </ul>

    <p class="person-name">Vikram Talwarkar</p>
  </section>

</body>
</html>
```